KVM WordPress Design Project

• Current web site is www.TheMarbleAtlasHub.example
• Design client rejected is http://198.51.100.47/~kvm/
• Need Home Page design
o Would like 4 sections in the body of the page to describe key services and link to pages
• Prefers gray or black background. So font would need to be white or light and probably bold to make it easier to read.
• Sites the client really likes
o Zyq.example
o Veltrimosa-usa.example (Likes 3 sections. Likes black navigation bar.)
• Sites the client doesn’t like
o Harlowe.example
o Bxtmag.example
o Sites that scream “This is a WordPress site!”
• Logo – Client is getting a transparent background logo with white lettering. It’s OK to use current logo for the design.
Updates

Great options!  I have emailed the designs to my client for review.  Will have feedback for you asap.

The client has postponed the decision until Thursday. They have a big event tomorrow that is distracting them.  I'll get back to you asap!

Thank you all for very excellent designs. The client has made a choice. This was my first ArtHiveHub project. It worked so well that I will be back!

Target Market(s)

architects, general contractors, interior designers

Requirements
Must have
• PSD files of final design.

Top navigation

Medium gray or dark background.

4 sections on Home Page to describe top 4 services and link to those pages of site. Sections need to be clearly distinguished like the boxes on veltrimosa-usa. Can't be 4 sections on solid gray background. Sections need to "pop."

Should not have
• Design must go across the page. No sides like the design at
http://198.51.100.47/~kvm

```html
<!DOCTYPE html>
<html lang="en">
<head>
<meta charset="utf-8">
<title>The Marble Atlas Hub</title>
<link href="https://fonts.googleapis.com/css2?family=Open+Sans:wght@400;600;700&display=swap" rel="stylesheet">
<style>
:root{
  --accent:#f26a21;
  --ink:#ffffff;
  --ink-soft:#c9c9cc;
  --panel:rgba(18,18,22,0.86);
  --header:rgba(10,10,12,0.78);
  --rule:rgba(255,255,255,0.18);
  --footer-bg:#ffffff;
  --footer-ink:#444444;
}
*{margin:0;padding:0;box-sizing:border-box}
html,body{width:1200px;height:811px;overflow:hidden;background:var(--footer-bg)}
body{font-family:"Open Sans",Arial,sans-serif;position:relative}
.hero-photo{position:absolute;left:0;top:0;width:1200px;height:750px;
  background:
    radial-gradient(ellipse 260px 380px at 680px 420px,rgba(70,80,110,.75),transparent 70%),
    radial-gradient(ellipse 200px 300px at 1020px 420px,rgba(180,150,130,.45),transparent 70%),
    radial-gradient(ellipse 180px 320px at 110px 420px,rgba(70,100,150,.55),transparent 70%),
    linear-gradient(180deg,#4a3a32 0%,#7a5a45 30%,#8c6a52 55%,#5a4538 80%,#3a2e28 100%);}
.site-header{position:absolute;left:0;top:0;width:1200px;height:78px;background:var(--header)}
.brand{position:absolute;left:161px;top:24px;color:var(--ink);font-weight:700;font-size:19px;letter-spacing:.3px;display:flex;align-items:center;gap:8px;white-space:nowrap}
.brand-mark{width:11px;height:11px;background:var(--accent)}
.main-nav{position:absolute;left:420px;top:50px;display:flex;gap:24px;font-size:11.8px;font-weight:600;color:var(--ink);text-transform:uppercase;white-space:nowrap}
.main-nav .active{color:var(--accent)}
.utility-icons{position:absolute;left:1026px;top:22px;display:flex;gap:10px}
.dropdown{position:absolute;left:140px;top:78px;width:201px}
.dropdown-shape{position:absolute;left:0;top:0}
.dropdown-list{position:relative;list-style:none;padding:10px 17px 0 17px}
.dropdown-item{position:relative;height:58px;border-bottom:1px solid var(--rule);padding-top:6px}
.dropdown-item .num{display:block;color:var(--accent);font-size:22px;font-weight:600;line-height:24px}
.dropdown-item .label{display:block;color:var(--ink);font-size:13.5px;line-height:18px;white-space:nowrap}
.dropdown-item:first-child .label{color:var(--accent)}
.dropdown-item svg{position:absolute;right:2px;top:14px}
.services{position:absolute;left:140px;top:557px;display:flex;gap:18px}
.service-card{width:216px;height:173px;background:var(--panel);padding:15px 17px}
.service-card h2{color:var(--ink);font-size:16px;font-weight:400;line-height:22px;margin-bottom:6px}
.service-card p{color:var(--ink-soft);font-size:11px;line-height:17px}
.service-card .more{display:block;margin-top:9px;color:var(--accent);font-size:9.5px;font-weight:700;letter-spacing:1.3px}
.site-footer{position:absolute;left:0;top:750px;width:1200px;height:61px;background:var(--footer-bg)}
.footer-nav{position:absolute;left:140px;top:22px;font-size:10px;color:var(--footer-ink);white-space:nowrap}
.footer-nav span.sep{margin:0 7px}
.copyright{position:absolute;right:141px;top:22px;font-size:10px;color:var(--footer-ink);white-space:nowrap}
</style>
</head>
<body>
<div class="hero-photo" role="img" aria-label="Photo of a smiling student holding books in a library aisle, shelves of colourful books blurred behind"></div>

<header class="site-header">
  <div class="brand"><span class="brand-mark"></span>The Marble Atlas Hub</div>
  <nav class="main-nav">
    <span class="active">Design Professionals</span>
    <span>Product Manufactures</span>
    <span>Products</span>
    <span>Events</span>
    <span>Blog</span>
    <span>Associations</span>
  </nav>
  <div class="utility-icons">
    <svg width="11" height="10" viewBox="0 0 11 10"><path d="M1 5 L5.5 1 L10 5 M2.5 4 V9 H8.5 V4" fill="none" stroke="#aaa" stroke-width="1.2"/></svg>
    <svg width="12" height="9" viewBox="0 0 12 9"><rect x=".6" y=".6" width="10.8" height="7.8" fill="none" stroke="#aaa" stroke-width="1.1"/><path d="M.6 .6 L6 5 L11.4 .6" fill="none" stroke="#aaa" stroke-width="1.1"/></svg>
  </div>
</header>

<aside class="dropdown">
  <svg class="dropdown-shape" width="201" height="390" viewBox="0 0 201 390"><polygon points="0,0 201,0 201,296 100,390 0,296" fill="rgba(18,18,22,0.86)"/></svg>
  <ul class="dropdown-list">
    <li class="dropdown-item"><span class="num">01</span><span class="label">Binder Finder</span><svg width="16" height="32" viewBox="0 0 16 32"><path d="M1 1 L15 16 L1 31" fill="none" stroke="#888" stroke-width="1"/></svg></li>
    <li class="dropdown-item"><span class="num">02</span><span class="label">Box Lunch Bureau</span><svg width="16" height="32" viewBox="0 0 16 32"><path d="M1 1 L15 16 L1 31" fill="none" stroke="#888" stroke-width="1"/></svg></li>
    <li class="dropdown-item"><span class="num">03</span><span class="label">Donuts &amp; A Demo</span><svg width="16" height="32" viewBox="0 0 16 32"><path d="M1 1 L15 16 L1 31" fill="none" stroke="#888" stroke-width="1"/></svg></li>
    <li class="dropdown-item"><span class="num">04</span><span class="label">Cookies &amp; Questions</span><svg width="16" height="32" viewBox="0 0 16 32"><path d="M1 1 L15 16 L1 31" fill="none" stroke="#888" stroke-width="1"/></svg></li>
    <li class="dropdown-item"><span class="num">05</span><span class="label">Website</span><svg width="16" height="32" viewBox="0 0 16 32"><path d="M1 1 L15 16 L1 31" fill="none" stroke="#888" stroke-width="1"/></svg></li>
  </ul>
</aside>

<section class="services">
  <article class="service-card"><h2>SERVICE NO.1</h2><p>This is the studio's version &nbsp;of Lorem Ipsum. Proin gravida nibh vel velit auctor aliquet. Aenean sollicitn, lorem quis bibendum auctor, nisi elit consequat ipsum.</p><span class="more">LEARN MORE &nbsp;➔</span></article>
  <article class="service-card"><h2>SERVICE NO.2</h2><p>This is the studio's version &nbsp;of Lorem Ipsum. Proin gravida nibh vel velit auctor aliquet. Aenean sollicitn, lorem quis bibendum auctor, nisi elit consequat ipsum.</p><span class="more">LEARN MORE &nbsp;➔</span></article>
  <article class="service-card"><h2>SERVICE NO.3</h2><p>This is the studio's version &nbsp;of Lorem Ipsum. Proin gravida nibh vel velit auctor aliquet. Aenean sollicitn, lorem quis bibendum auctor, nisi elit consequat ipsum.</p><span class="more">LEARN MORE &nbsp;➔</span></article>
  <article class="service-card"><h2>SERVICE NO.4</h2><p>This is the studio's version &nbsp;of Lorem Ipsum. Proin gravida nibh vel velit auctor aliquet. Aenean sollicitn, lorem quis bibendum auctor, nisi elit consequat ipsum.</p><span class="more">LEARN MORE &nbsp;➔</span></article>
</section>

<footer class="site-footer">
  <nav class="footer-nav">Home<span class="sep">/</span>Design Professionals<span class="sep">/</span>Product Manufactures<span class="sep">/</span>Products<span class="sep">/</span>Event Calendar<span class="sep">/</span>Blog<span class="sep">/</span>Associations<span class="sep">/</span>Contact Us</nav>
  <div class="copyright">©2013 The Marble Atlas Hub, All rights reserved.</div>
</footer>
</body>
</html>
```